Quarrydeen Fintech Product Infographic

Quarrydeen is an established Fintech business, supplying complex financial software to banks and building societies.

We currently have a picture/infographic to show each of our 11 different software products in a single image. Each product can be installed on its own as a standalone application or if multiple products are installed they will share data.

The key message for our infographic is to convey the integration via a shared database.

The attached diagram is what we currently use which is to give you an idea of the message we are trying to give, but we are not tied to this format and are looking for this diagram to be reimagined.

We will look to use our new chosen design on printed media such as A4 Data sheets an example of which is attached.

For more information on our products please refer to www.quarrydeen.co.uk/products

```html
<!DOCTYPE html>
<html lang="en">
<head>
<meta charset="utf-8">
<title>Quarrydeen Fintech Product Infographic</title>
<link href="https://fonts.googleapis.com/css2?family=Inter:wght@400;700&display=swap" rel="stylesheet">
<style>
  :root {
    --performance: #c077b2;
    --performance-soft: #f4e9f2;
    --finance: #4cbceb;
    --finance-soft: #e4f4fb;
    --risk: #fdbe53;
    --risk-soft: #fef4e5;
    --regulatory: #0eb9a4;
    --regulatory-soft: #ddf5f1;
    --core: #253b7a;
    --core-soft: #dfe3ec;
    --dots: #d5d8de;
    --bg: #ffffff;
  }
  html, body { margin: 0; padding: 0; overflow: hidden; background: var(--bg); }
  .infographic { display: block; width: 1200px; height: 849px; font-family: "Inter", sans-serif; }
  .product-label { font-size: 28px; fill: #fff; text-anchor: middle; font-weight: 400; }
  .group-title { font-size: 25px; font-weight: 700; text-anchor: middle; }
  .core-title { font-size: 36px; font-weight: 700; text-anchor: middle; fill: var(--core); }
  .connector { fill: none; stroke: var(--dots); stroke-width: 4; stroke-dasharray: 1 9; stroke-linecap: round; }
  .node { fill: #fff; stroke-width: 3; }
  .node-core { fill: var(--core); }
  .performance .ring { stroke: var(--performance); } .performance .band { stroke: var(--performance-soft); }
  .performance .product { fill: var(--performance); } .performance .group-title { fill: var(--performance); }
  .performance .icon { stroke: var(--performance); }
  .finance .ring { stroke: var(--finance); } .finance .band { stroke: var(--finance-soft); }
  .finance .product { fill: var(--finance); } .finance .group-title { fill: var(--finance); }
  .finance .icon { stroke: var(--finance); }
  .risk .ring { stroke: var(--risk); } .risk .band { stroke: var(--risk-soft); }
  .risk .product { fill: var(--risk); } .risk .group-title { fill: var(--risk); }
  .risk .icon { stroke: var(--risk); }
  .regulatory .ring { stroke: var(--regulatory); } .regulatory .band { stroke: var(--regulatory-soft); }
  .regulatory .product { fill: var(--regulatory); } .regulatory .group-title { fill: var(--regulatory); }
  .regulatory .icon { stroke: var(--regulatory); }
  .ring { fill: none; stroke-width: 3; }
  .band { fill: none; stroke-width: 44; }
  .icon { fill: none; stroke-width: 3; stroke-linecap: round; stroke-linejoin: round; }
  .core .ring { stroke: var(--core); stroke-width: 4; }
  .core .band { stroke: var(--core-soft); }
</style>
</head>
<body>
<svg class="infographic" viewBox="0 0 1750 1238" preserveAspectRatio="xMidYMid meet" xmlns="http://www.w3.org/2000/svg">

  <!-- connectors -->
  <path class="connector" d="M566 360 H872 V439"/>
  <path class="connector" d="M657 647 H340 V726"/>
  <path class="connector" d="M1090 647 H1416 V587"/>
  <path class="connector" d="M872 870 V955 H1186"/>

  <!-- performance -->
  <g class="performance">
    <circle class="band" cx="341" cy="360" r="192"/>
    <circle class="ring" cx="341" cy="360" r="224"/>
    <circle class="product" cx="343" cy="165" r="92"/>
    <circle class="product" cx="175" cy="468" r="92"/>
    <circle class="product" cx="502" cy="468" r="92"/>
    <text class="product-label" x="343" y="165"><tspan x="343" dy="-4">Financial</tspan><tspan x="343" dy="32">Planning</tspan></text>
    <text class="product-label" x="175" y="452"><tspan x="175" dy="0">Funds</tspan><tspan x="175" dy="32">Transfer</tspan><tspan x="175" dy="32">Pricing</tspan></text>
    <text class="product-label" x="502" y="468"><tspan x="502" dy="0">Business</tspan><tspan x="502" dy="32">Intelligence</tspan></text>
    <path class="icon" d="M362 292 L330 300 L316 330 L334 342 L360 322 Z M318 322 L310 336 L324 332 M332 340 L346 346 L346 332"/>
    <circle class="icon" cx="343" cy="312" r="5"/>
    <text class="group-title" x="343" y="391">PERFORMANCE</text>
    <circle class="node" cx="566" cy="360" r="9" stroke="var(--performance)"/>
    <circle cx="566" cy="360" r="3" fill="var(--performance)"/>
  </g>

  <!-- finance -->
  <g class="finance">
    <circle class="band" cx="1406" cy="360" r="192"/>
    <circle class="ring" cx="1406" cy="360" r="224"/>
    <circle class="product" cx="1416" cy="165" r="92"/>
    <circle class="product" cx="1238" cy="468" r="92"/>
    <circle class="product" cx="1569" cy="468" r="92"/>
    <text class="product-label" x="1416" y="165"><tspan x="1416" dy="-4">Financial</tspan><tspan x="1416" dy="32">Ledgers</tspan></text>
    <text class="product-label" x="1237" y="452"><tspan x="1237" dy="0">Effective</tspan><tspan x="1237" dy="32">Interest</tspan><tspan x="1237" dy="32">Rates</tspan></text>
    <text class="product-label" x="1570" y="468"><tspan x="1570" dy="0">Hedge</tspan><tspan x="1570" dy="32">Accounting</tspan></text>
    <circle class="icon" cx="1407" cy="326" r="28"/>
    <path class="icon" d="M1416 316 Q1407 308 1399 316 Q1396 325 1407 326 Q1418 327 1415 336 Q1407 344 1398 336 M1407 306 V346"/>
    <text class="group-title" x="1416" y="390">FINANCE</text>
    <circle class="node" cx="1416" cy="587" r="9" stroke="var(--finance)"/>
    <circle cx="1416" cy="587" r="3" fill="var(--finance)"/>
  </g>

  <!-- risk -->
  <g class="risk">
    <circle class="band" cx="340" cy="950" r="192"/>
    <circle class="ring" cx="340" cy="950" r="224"/>
    <circle class="product" cx="155" cy="953" r="92"/>
    <circle class="product" cx="527" cy="953" r="92"/>
    <text class="product-label" x="155" y="967">Treasury</text>
    <text class="product-label" x="532" y="967">ALM</text>
    <rect class="icon" x="316" y="898" width="48" height="34"/>
    <path class="icon" d="M340 932 V952 M330 952 L340 942 L350 952 M324 906 L330 912 M330 906 L324 912 M328 924 Q342 924 350 908"/>
    <text class="group-title" x="343" y="996">RISK</text>
    <circle class="node" cx="340" cy="726" r="9" stroke="var(--risk)"/>
    <circle cx="340" cy="726" r="3" fill="var(--risk)"/>
  </g>

  <!-- regulatory -->
  <g class="regulatory">
    <circle class="band" cx="1410" cy="955" r="192"/>
    <circle class="ring" cx="1410" cy="955" r="224"/>
    <circle class="product" cx="1418" cy="757" r="92"/>
    <circle class="product" cx="1245" cy="1060" r="92"/>
    <circle class="product" cx="1575" cy="1060" r="92"/>
    <text class="product-label" x="1420" y="757"><tspan x="1420" dy="-4">Regulatory</tspan><tspan x="1420" dy="32">Reporting</tspan></text>
    <text class="product-label" x="1244" y="1056"><tspan x="1244" dy="0">FSCS</tspan><tspan x="1244" dy="32">SCV</tspan></text>
    <text class="product-label" x="1577" y="1060"><tspan x="1577" dy="0">Taxation</tspan><tspan x="1577" dy="32">Reporting</tspan></text>
    <path class="icon" d="M1418 904 V946 M1404 946 H1432 M1396 910 H1440 M1396 910 L1390 926 H1402 Z M1440 910 L1434 926 H1446 Z"/>
    <text class="group-title" x="1418" y="999">REGULATORY</text>
    <circle class="node" cx="1186" cy="955" r="9" stroke="var(--regulatory)"/>
    <circle cx="1186" cy="955" r="3" fill="var(--regulatory)"/>
  </g>

  <!-- shared data core -->
  <g class="core">
    <circle class="band" cx="872" cy="655" r="182"/>
    <circle class="ring" cx="872" cy="655" r="215"/>
    <rect x="760" y="528" width="228" height="185" rx="20" fill="#dfe1f4" role="img" aria-label="Illustration of three database servers"/>
    <text class="core-title" x="872" y="752">SHARED</text>
    <text class="core-title" x="872" y="786">DATA</text>
    <g>
      <circle class="node" cx="872" cy="439" r="9" stroke="var(--core)"/><circle class="node-core" cx="872" cy="439" r="3"/>
      <circle class="node" cx="657" cy="647" r="9" stroke="var(--core)"/><circle class="node-core" cx="657" cy="647" r="3"/>
      <circle class="node" cx="1090" cy="647" r="9" stroke="var(--core)"/><circle class="node-core" cx="1090" cy="647" r="3"/>
      <circle class="node" cx="872" cy="870" r="9" stroke="var(--core)"/><circle class="node-core" cx="872" cy="870" r="3"/>
    </g>
  </g>
</svg>
</body>
</html>
```